Tovrin

My company name is pebble. The logo is attached. I am the business owner.
Name Gideon Thorpe
Phone number- 5553018826
email- Gideon_thorpe@quillnet.net
Website is not live yet but it will be tovrinhires.com
the current beta link is- https://site.brvhosting.com/pebble-v3/
on the back write “ Meet skilled makers”
Use that beta link as reference for typography and colors on card.

```html
<!DOCTYPE html>
<html lang="en">
<head>
<meta charset="utf-8">
<title>Tovrin Business Card</title>
<link href="https://fonts.googleapis.com/css2?family=Arimo:wght@400;700&display=swap" rel="stylesheet">
<style>
  :root {
    --backdrop: #808080;
    --card: #111111;
    --accent: #c8461b;
    --wordmark-front: #d9d9d9;
    --wordmark-back: #ffffff;
    --contact-text: #b5b5b5;
    --shadow: rgba(0, 0, 0, 0.45);
  }
  html, body {
    margin: 0;
    padding: 0;
    overflow: hidden;
  }
  .canvas {
    position: relative;
    width: 1065px;
    height: 1200px;
    background: var(--backdrop);
    font-family: "Arimo", Arial, sans-serif;
    overflow: hidden;
  }
  .card {
    position: absolute;
    height: 363px;
    background: var(--card);
    box-shadow: 2px 3px 3px var(--shadow);
  }
  .card--front {
    left: 292px;
    top: 218px;
    width: 585px;
    border-radius: 0 182px 182px 0;
  }
  .card--back {
    left: 263px;
    top: 623px;
    width: 583px;
    border-radius: 182px 0 0 182px;
  }
  .holder-name {
    position: absolute;
    left: 53px;
    top: 52px;
    margin: 0;
    font-size: 21px;
    font-weight: 700;
    color: var(--accent);
    letter-spacing: 0.2px;
  }
  .wordmark {
    position: absolute;
    margin: 0;
    font-weight: 700;
    line-height: 1;
    letter-spacing: -1px;
  }
  .card--front .wordmark {
    left: 291px;
    top: 143px;
    font-size: 58px;
    color: var(--wordmark-front);
  }
  .contact-list {
    position: absolute;
    left: 52px;
    top: 241px;
    margin: 0;
    padding: 0;
    list-style: none;
  }
  .contact-item {
    display: flex;
    align-items: center;
    height: 24px;
    margin-bottom: 4.5px;
    font-size: 16.5px;
    color: var(--contact-text);
  }
  .contact-icon {
    width: 24px;
    height: 24px;
    margin-right: 7px;
    flex: none;
  }
  .back-lockup {
    position: absolute;
    left: 0;
    right: 0;
    top: 128px;
    text-align: center;
  }
  .card--back .wordmark {
    position: static;
    font-size: 77px;
    color: var(--wordmark-back);
    letter-spacing: -1.5px;
    padding-left: 12px;
  }
  .tagline {
    margin: 10px 0 0 12px;
    font-size: 21px;
    font-weight: 700;
    color: var(--wordmark-back);
    letter-spacing: 3.2px;
  }
</style>
</head>
<body>
<div class="canvas">
  <section class="card card--front">
    <h1 class="holder-name">GIDEON THORPE</h1>
    <p class="wordmark">TOVRIN</p>
    <ul class="contact-list">
      <li class="contact-item">
        <svg class="contact-icon" viewBox="0 0 24 24" aria-hidden="true">
          <circle cx="12" cy="12" r="12" fill="var(--accent)"/>
          <path d="M8.2 6.5l2 2.3-1.1 1.3c.8 1.7 2 2.9 3.7 3.7l1.3-1.1 2.3 2-1.2 1.8c-4.2-.4-8.2-4.4-8.6-8.6z" fill="none" stroke="#111" stroke-width="1.3" stroke-linejoin="round"/>
        </svg>
        <span>5553018826</span>
      </li>
      <li class="contact-item">
        <svg class="contact-icon" viewBox="0 0 24 24" aria-hidden="true">
          <circle cx="12" cy="12" r="12" fill="var(--accent)"/>
          <rect x="6" y="8" width="12" height="8.5" fill="none" stroke="#111" stroke-width="1.2"/>
          <path d="M6 8l6 5 6-5M6 16.5l4.5-4.3M18 16.5l-4.5-4.3" fill="none" stroke="#111" stroke-width="1.1"/>
        </svg>
        <span>Gideon_thorpe@quillnet.net</span>
      </li>
      <li class="contact-item">
        <svg class="contact-icon" viewBox="0 0 24 24" aria-hidden="true">
          <circle cx="12" cy="12" r="12" fill="var(--accent)"/>
          <g fill="none" stroke="#111" stroke-width="1.1">
            <circle cx="12" cy="12" r="5.8"/>
            <ellipse cx="12" cy="12" rx="2.6" ry="5.8"/>
            <path d="M6.2 12h11.6M7 9h10M7 15h10M12 6.2v11.6"/>
          </g>
        </svg>
        <span>www.tovrinhires.com</span>
      </li>
    </ul>
  </section>

  <section class="card card--back">
    <div class="back-lockup">
      <p class="wordmark">TOVRIN</p>
      <p class="tagline">MEET SKILLED MAKERS</p>
    </div>
  </section>
</div>
</body>
</html>
```